Bar and Grill needs specials signage

I have attached a file called "daily specials" I need it changed - so there is 1 sign/poster for each day/special
also attached other items to show some styling. I want the new posters chalkboard format, styled along the lines of the drink designs attached.
The designs should be scaleable, and editable, I will print locally

```html
<!DOCTYPE html>
<html lang="en">
<head>
<meta charset="utf-8">
<title>Daily Specials – Weekend Chalkboard Posters</title>
<link rel="stylesheet" href="https://fonts.googleapis.com/css2?family=Playball&family=Oranienbaum&family=Bevan&family=Oswald:wght@400;600;700&family=Abril+Fatface&family=Kaushan+Script&family=Lobster+Two:wght@700&family=Old+Standard+TT:wght@400;700&family=IM+Fell+English&display=swap">
<style>
  :root {
    --backdrop: #5e5e5e;
    --board: #262422;
    --board-edge: #1b1a19;
    --chalk: #f2efe8;
    --chalk-soft: rgba(242, 239, 232, 0.75);
    --teal: #6fbfae;
    --orange: #e59a4c;
    --pink: #e58bb0;
  }
  * { margin: 0; padding: 0; box-sizing: border-box; }
  html, body { width: 1200px; height: 640px; overflow: hidden; background: var(--backdrop); }
  .poster-row { position: relative; width: 1200px; height: 640px; }
  .poster {
    position: absolute; top: 90px; width: 355px; height: 460px;
    background: radial-gradient(ellipse at 50% 40%, #33302d 0%, var(--board) 55%, var(--board-edge) 100%);
    box-shadow: 4px 6px 10px rgba(0,0,0,0.45);
    color: var(--chalk); text-align: center; overflow: hidden;
  }
  .poster--friday { left: 44px; --accent: var(--teal); }
  .poster--saturday { left: 422px; --accent: var(--orange); }
  .poster--sunday { left: 802px; --accent: var(--pink); }

  .frame { position: absolute; inset: 0; }
  .frame path, .frame line { stroke: var(--chalk-soft); stroke-width: 1.2; fill: none; stroke-linecap: round; }
  .frame .accent-dash { stroke: var(--accent); stroke-dasharray: 2 2; }

  .header-daily {
    position: absolute; top: 26px; left: 0; right: 0;
    font: 42px/1 "Playball", cursive;
  }
  .header-specials {
    position: absolute; top: 72px; left: 0; right: 0;
    font: 38px/1 "Oranienbaum", serif; letter-spacing: 1px;
  }
  .day {
    position: absolute; top: 168px; left: 0; right: 0;
    font-size: 50px; line-height: 1; color: var(--accent);
  }
  .poster--friday .day {
    font-family: "Bevan", serif; letter-spacing: 6px; font-size: 44px; top: 172px;
    color: transparent; -webkit-text-stroke: 1.6px var(--accent);
  }
  .poster--saturday .day {
    font-family: "Oswald", sans-serif; font-weight: 700; letter-spacing: 2px; font-size: 54px; top: 162px;
    text-shadow: 2px 2px 0 rgba(0,0,0,0.6), 3px 3px 0 rgba(229,154,76,0.35);
  }
  .poster--sunday .day {
    font-family: "Abril Fatface", serif; letter-spacing: 5px; font-size: 50px; top: 166px;
    text-shadow: 3px 3px 0 rgba(229,139,176,0.3);
  }

  .dish { position: absolute; left: 0; right: 0; }
  .fish-title { top: 248px; font: 40px/1 "Kaushan Script", cursive; color: var(--accent); }
  .fish-desc { top: 296px; font: 700 22px/1.25 "Lobster Two", cursive; }
  .oven-title { top: 262px; font: 26px/1 "Old Standard TT", serif; color: var(--accent); letter-spacing: 2px; }
  .oven-line { font-family: "Oswald", sans-serif; letter-spacing: 0.5px; }
  .oven-main { top: 292px; font-size: 19px; font-weight: 400; }
  .oven-sub { top: 320px; font-size: 14.5px; }
  .oven-side { top: 345px; font-size: 11.5px; }
  .chicken-title { top: 256px; font: 25px/1 "IM Fell English", serif; }
  .chicken-desc { top: 290px; font: 15.5px/1.7 "Old Standard TT", serif; letter-spacing: 1px; }

  .illustration {
    position: absolute; left: 60px; right: 60px; top: 352px; height: 82px;
    background: radial-gradient(ellipse at center, rgba(255,255,255,0.08), rgba(255,255,255,0) 70%);
    border-radius: 6px;
  }
  .poster--saturday .illustration { top: 362px; height: 76px; }
</style>
</head>
<body>
<main class="poster-row">

  <!-- Friday -->
  <section class="poster poster--friday">
    <svg class="frame" viewBox="0 0 355 460" aria-hidden="true">
      <path d="M20 60 V28 H60 M20 28 L30 38"/><path d="M335 60 V28 H295 M335 28 L325 38"/>
      <path d="M60 90 Q177 60 295 90 L270 132 H85 Z"/>
      <line class="accent-dash" x1="100" y1="138" x2="255" y2="138"/>
      <path d="M171 120 v42 M168 120 v12 M174 120 v12 M184 120 q4 10 0 20 v22 M160 122 a4 6 0 1 0 0.1 0 M160 134 v28"/>
      <line x1="12" y1="148" x2="343" y2="148"/>
      <line x1="20" y1="148" x2="20" y2="440"/><line x1="335" y1="148" x2="335" y2="440"/>
      <line x1="40" y1="222" x2="315" y2="222"/>
      <line class="accent-dash" x1="65" y1="236" x2="290" y2="236"/>
      <path d="M20 440 H60 M335 440 H295"/>
    </svg>
    <div class="header-daily">Daily</div>
    <div class="header-specials">SPECIALS</div>
    <h2 class="day">FIRDAY</h2>
    <div class="dish fish-title">Fish &amp; Chips</div>
    <div class="dish fish-desc">beer buttered cod fish<br>and steak fries</div>
    <div class="illustration" role="img" aria-label="Chalk drawing of a cod fish, small fish and ice cubes"></div>
  </section>

  <!-- Saturday -->
  <section class="poster poster--saturday">
    <svg class="frame" viewBox="0 0 355 460" aria-hidden="true">
      <path d="M20 60 V28 H60 M20 28 L30 38"/><path d="M335 60 V28 H295 M335 28 L325 38"/>
      <path d="M60 90 Q177 60 295 90 L270 132 H85 Z"/>
      <line class="accent-dash" x1="100" y1="138" x2="255" y2="138"/>
      <path d="M171 120 v42 M168 120 v12 M174 120 v12 M184 120 q4 10 0 20 v22 M160 122 a4 6 0 1 0 0.1 0 M160 134 v28"/>
      <line x1="12" y1="148" x2="343" y2="148"/>
      <line x1="20" y1="148" x2="20" y2="440"/><line x1="335" y1="148" x2="335" y2="440"/>
      <line x1="40" y1="226" x2="315" y2="226"/>
      <line class="accent-dash" x1="65" y1="240" x2="290" y2="240"/>
      <path d="M20 440 H60 M335 440 H295"/>
    </svg>
    <div class="header-daily">Daily</div>
    <div class="header-specials">SPECIALS</div>
    <h2 class="day">SATURDAY</h2>
    <div class="dish oven-title">“DUTCH OVEN”</div>
    <div class="dish oven-line oven-main">BONELESS BEEF SHORT RIBS</div>
    <div class="dish oven-line oven-sub">CHIPOTLE BBQ SAUCE &amp; CRISPY ONIONS,</div>
    <div class="dish oven-line oven-side">GARLIC MASHED POTATOES, FREASH VEGETABLE</div>
    <div class="illustration" role="img" aria-label="Chalk drawing of two bulls either side of a flame with crossed cleavers"></div>
  </section>

  <!-- Sunday -->
  <section class="poster poster--sunday">
    <svg class="frame" viewBox="0 0 355 460" aria-hidden="true">
      <path d="M20 60 V28 H60 M20 28 L30 38"/><path d="M335 60 V28 H295 M335 28 L325 38"/>
      <path d="M60 90 Q177 60 295 90 L270 132 H85 Z"/>
      <line class="accent-dash" x1="100" y1="138" x2="255" y2="138"/>
      <path d="M171 120 v42 M168 120 v12 M174 120 v12 M184 120 q4 10 0 20 v22 M160 122 a4 6 0 1 0 0.1 0 M160 134 v28"/>
      <line x1="12" y1="148" x2="343" y2="148"/>
      <line x1="20" y1="148" x2="20" y2="440"/><line x1="335" y1="148" x2="335" y2="440"/>
      <line x1="40" y1="222" x2="315" y2="222"/>
      <line class="accent-dash" x1="65" y1="236" x2="290" y2="236"/>
      <path d="M20 440 H60 M335 440 H295"/>
    </svg>
    <div class="header-daily">Daily</div>
    <div class="header-specials">SPECIALS</div>
    <h2 class="day">SUNDAY</h2>
    <div class="dish chicken-title">Crisped Fried Chicken</div>
    <div class="dish chicken-desc">MASHED POTATOES AND<br>GRAVY WITH A VEGETABLE</div>
    <div class="illustration" role="img" aria-label="Chalk drawing of a bowl of mashed potatoes, a roast chicken on a plate and a vegetable dish"></div>
  </section>

</main>
</body>
</html>
```